Tess Marlowe Communication business card

I am starting a small, country-based business that offers writing, communication and marketing services to a wide range of clients, inner city big business, to mining, through to agriculture.

The appeal of my business is that it's mobile and flexible. It's just me, with lots of hands-on experience on construction and infrastructure projects.

I can provide the following services:

• Communication planning and management
• Issues and media management
• Marketing and communication materials
• Project management and strategy
• Government liaison
• Incident management communication
• Stakeholder management

It would be great to be able to use the elements of the business card design on other stationery.

Industry/Entity Type

Communication

Requirements
Must have
• The following information:

Tess Marlowe
M: 0427 391 864
E: tess@tmcommsmail.com

PO Box 152
Durrandale Q 4472
Nice to have
• a rural element (windmill, workboots, wheat stalk)

```html
<!DOCTYPE html>
<html lang="en">
<head>
<meta charset="utf-8">
<title>Tess Marlowe Communication – Business Card</title>
<link rel="stylesheet" href="https://fonts.googleapis.com/css2?family=Anton&family=Oswald:wght@600&family=Arimo:wght@700&display=swap">
<style>
  :root {
    --page: #ffffff;
    --card-border: #8fcf9a;
    --cream: #f8e6c4;
    --pale-green: #d3e9b6;
    --wheat-gold: #e0a545;
    --wheat-rust: #c06a2a;
    --leaf-green: #7dc242;
    --text-green: #6db33f;
    --text-shadow: rgba(90, 110, 40, 0.45);
  }
  * { margin: 0; padding: 0; box-sizing: border-box; }
  html, body {
    width: 1200px;
    height: 848px;
    overflow: hidden;
    background: var(--page);
  }
  .business-card {
    position: absolute;
    left: 19px;
    top: 108px;
    width: 1147px;
    height: 633px;
    border: 1px solid var(--card-border);
    overflow: hidden;
    background: linear-gradient(100deg, var(--cream) 0%, #f1e6c2 45%, var(--pale-green) 100%);
  }
  .wheat-artwork {
    position: absolute;
    inset: 0;
    width: 100%;
    height: 100%;
  }
  .card-name {
    position: absolute;
    top: 8px;
    left: 0;
    width: 100%;
    text-align: center;
    font-family: "Anton", "Oswald", sans-serif;
    font-size: 152px;
    line-height: 1.1;
    letter-spacing: 10px;
    color: var(--leaf-green);
    text-shadow: 1px 1px 0 #ffffff, 2px 2px 3px var(--text-shadow);
  }
  .service-list {
    position: absolute;
    top: 236px;
    left: 0;
    width: 100%;
    list-style: none;
    text-align: center;
    font-family: "Oswald", "Arial Narrow", sans-serif;
    font-weight: 600;
    font-size: 29px;
    line-height: 45px;
    letter-spacing: 1.2px;
    color: var(--text-green);
    text-shadow: 1px 1px 2px var(--text-shadow);
  }
  .service-list li { display: block; }
  .contact-details {
    position: absolute;
    left: 579px;
    top: 507px;
    font-family: "Arimo", Arial, sans-serif;
    font-weight: 700;
    font-size: 25px;
    line-height: 35px;
    letter-spacing: 2px;
    color: var(--text-green);
    font-style: normal;
  }
  .contact-details .gap { display: inline-block; width: 38px; }
</style>
</head>
<body>
  <section class="business-card">
    <svg class="wheat-artwork" viewBox="0 0 1147 633" preserveAspectRatio="none" role="img" aria-label="Golden wheat stalks sweeping up from the lower left corner">
      <defs>
        <radialGradient id="wheat-glow" cx="0.05" cy="0.95" r="0.9">
          <stop offset="0" stop-color="var(--wheat-rust)" stop-opacity="0.85"/>
          <stop offset="0.35" stop-color="var(--wheat-gold)" stop-opacity="0.6"/>
          <stop offset="0.75" stop-color="var(--wheat-gold)" stop-opacity="0.18"/>
          <stop offset="1" stop-color="var(--wheat-gold)" stop-opacity="0"/>
        </radialGradient>
      </defs>
      <path d="M0 633 L0 180 C250 150 700 60 1147 20 L1147 260 C800 330 450 470 330 633 Z" fill="url(#wheat-glow)"/>
    </svg>

    <h1 class="card-name">Tess Marlowe</h1>

    <ul class="service-list">
      <li>• Communication planning and management &nbsp;• Issues and media management</li>
      <li>• Marketing and communication materials &nbsp;• Project management and strategy</li>
      <li>• Government liaison &nbsp;• Incident management communication</li>
      <li>• Stakeholder management</li>
    </ul>

    <address class="contact-details">
      <div class="postal">PO Box 152<span class="gap"></span>Durrandale Q 4472</div>
      <div class="mobile">Mobile number : 0427 391 864</div>
      <div class="email">E-mail : tess@tmcommsmail.com</div>
    </address>
  </section>
</body>
</html>
```